Business cards for a new business: Willow Brook Calm Healing

I would like for the card to include a lotus. The business is a healing practice so I'd like the overall colours to be pink and green and for it to have a soft feel. The name of the practice is
"Willow Brook Calm Healing", which I'd like to be included, as well as the words: "Energetic and spiritual healing to restore health, harmony and wellbeing". Also, my name - Tarik and the number: 5391 6048

Target Market(s)

Everyone interested in personal healing!

Industry/Entity Type

Business

Contact Information for Business Card

As above……..could be single or double-sided
I'd like the font for the name of the practice and my name to be in green and be a flowing, but simple font - elegant.
The background to be a light pink. See below for colours

Colors
f9d9e8
eea4c8
e567a6
d0ebe7
86cfc6
33b7a4

Requirements
Must have
• See above
Nice to have
• See above

```html
<!DOCTYPE html>
<html lang="en">
<head>
<meta charset="utf-8">
<title>Tarik – Business Card</title>
<link rel="stylesheet" href="https://fonts.googleapis.com/css2?family=Arimo:wght@400;700&display=swap">
<style>
  :root {
    --page-bg: #ece8e6;
    --card-bg: #fbfbfa;
    --name-green: #3dbb84;
    --phone-green: #4cc08e;
    --text-dark: #222222;
    --hands-light: #f4eeee;
    --hands-mid: #d9a8a8;
    --practice-ink: #3a2630;
  }
  * { box-sizing: border-box; margin: 0; padding: 0; }
  html, body {
    width: 1200px;
    height: 818px;
    overflow: hidden;
    background: var(--page-bg);
    font-family: "Arimo", Arial, sans-serif;
  }
  .canvas {
    position: relative;
    width: 1200px;
    height: 818px;
  }
  .card {
    position: absolute;
    left: 380px;
    top: 49px;
    width: 440px;
    height: 720px;
    background: var(--card-bg);
    box-shadow: 0 6px 24px rgba(0,0,0,0.12);
    text-align: center;
  }
  .card__hands {
    position: absolute;
    left: 0;
    top: 40px;
    width: 440px;
    height: 250px;
    background: radial-gradient(ellipse 60% 50% at 50% 50%, var(--hands-mid) 0%, var(--hands-light) 70%, var(--card-bg) 100%);
    opacity: 0.85;
  }
  .card__practice {
    position: absolute;
    left: 0;
    right: 0;
    top: 316px;
    display: flex;
    align-items: center;
    justify-content: center;
    gap: 10px;
    font-size: 21px;
    font-weight: 700;
    color: var(--practice-ink);
    line-height: 1;
  }
  .card__practice-dot {
    width: 14px;
    height: 14px;
    border-radius: 50%;
    background: var(--practice-ink);
  }
  .card__name {
    position: absolute;
    left: 0;
    right: 0;
    top: 362px;
    font-size: 86px;
    font-weight: 700;
    color: var(--name-green);
    letter-spacing: 1px;
    line-height: 1;
  }
  .card__phone {
    position: absolute;
    left: 0;
    right: 0;
    top: 462px;
    font-size: 42px;
    font-weight: 400;
    color: var(--phone-green);
    letter-spacing: 2px;
    line-height: 1;
  }
  .card__tagline {
    position: absolute;
    left: 20px;
    right: 20px;
    top: 556px;
    font-size: 21px;
    line-height: 1.3;
    color: var(--text-dark);
  }
</style>
</head>
<body>
  <div class="canvas">
    <div class="card">
      <div class="card__hands" role="img" aria-label="Photograph of two open hands cupped around healing energy"></div>
      <div class="card__practice">
        <span class="card__practice-dot"></span>
        <span class="card__practice-name">Willow Brook Calm Healing</span>
      </div>
      <div class="card__name">Tarik</div>
      <div class="card__phone">5391 6048</div>
      <p class="card__tagline">Energetic &amp; Spiritual healing to restore<br>health, harmony and wellbeing</p>
    </div>
  </div>
</body>
</html>
```